Birchford Realty Business Card

Business Card:

Somewhere on front of card, please include Broker License Number: 5839162

Website is BirchfordRealty.example

Address is:
7218 Crestover Ave E
Saginaw, MI 48271

I'll let you use creative freedom on the rest; we obviously need Name, Title, Email (jordan@BirchfordRealty.example), Office Phone, Cell Phone.

Don't want any special die-cutting, just a standard size business card.

On the back, include a place for the date and time of an appointment to be written in pen.

Requirements
Must have
• Our logo, attached to email.

```html
<!DOCTYPE html>
<html lang="en">
<head>
<meta charset="utf-8">
<title>Birchford Realty Business Card</title>
<link rel="stylesheet" href="https://fonts.googleapis.com/css2?family=Open+Sans:wght@600;700&display=swap">
<style>
  :root {
    --navy: #2a2a7a;
    --white: #ffffff;
    --paper-light: #ebebec;
    --paper-shade: #d2d2d5;
    --backdrop: #f2f2f2;
  }
  * { margin: 0; padding: 0; box-sizing: border-box; }
  html, body {
    width: 1066px;
    height: 1200px;
    overflow: hidden;
    background: var(--backdrop);
    font-family: "Open Sans", Arial, sans-serif;
  }
  .canvas { position: relative; width: 1066px; height: 1200px; }
  .card {
    position: absolute;
    left: 253px;
    width: 559px;
    height: 308px;
    border-radius: 16px;
    overflow: hidden;
  }
  .card-shapes { position: absolute; inset: 0; width: 100%; height: 100%; display: block; }
  .card-front { top: 228px; background: var(--navy); }
  .card-back {
    top: 640px;
    background: linear-gradient(90deg, var(--paper-light) 0 50%, var(--paper-shade) 50% 100%);
  }
  .brand-name {
    position: absolute;
    font-weight: 700;
    white-space: nowrap;
    letter-spacing: -0.2px;
  }
  .card-front .brand-name { left: 75px; top: 206px; font-size: 20px; color: var(--white); }
  .card-back .brand-name { right: 301px; top: 134px; font-size: 23px; color: var(--navy); }
  .appointment {
    position: absolute;
    left: 301px;
    top: 210px;
    width: 243px;
    height: 81px;
    padding: 8px 12px;
    color: var(--navy);
    font-size: 12px;
    font-weight: 700;
    line-height: 21px;
  }
  .appointment-field { display: flex; gap: 6px; }
  .write-line { flex: 1; border-bottom: 1px solid var(--navy); margin-bottom: 5px; }
  .details {
    position: absolute;
    left: 290px;
    top: 56px;
    color: var(--navy);
    font-weight: 700;
    white-space: nowrap;
  }
  .agent-name { font-size: 17px; line-height: 21px; }
  .agent-title { font-size: 13.5px; line-height: 20px; }
  .address {
    margin-top: 2px;
    font-size: 13px;
    line-height: 18px;
    font-style: normal;
    font-weight: 600;
    color: var(--white);
  }
  .contact-list { list-style: none; margin-top: 36px; font-size: 12.5px; line-height: 18px; }
</style>
</head>
<body>
<main class="canvas">
  <section class="card card-front" aria-label="Card back side">
    <svg class="card-shapes" viewBox="0 0 490 270" preserveAspectRatio="none" aria-hidden="true">
      <polygon points="128,0 245,50 358,0 330,0 245,37 158,0" fill="var(--white)"/>
      <rect x="264" y="184" width="213" height="71" fill="var(--white)"/>
    </svg>
    <div class="brand-name">Birchford Realty</div>
    <div class="appointment">
      <div>Your appointment</div>
      <div class="appointment-field"><span>Date:</span><span class="write-line"></span></div>
      <div class="appointment-field"><span>Time:</span><span class="write-line"></span></div>
    </div>
  </section>

  <section class="card card-back" aria-label="Card front side">
    <svg class="card-shapes" viewBox="0 0 490 270" preserveAspectRatio="none" aria-hidden="true">
      <polygon points="133,0 246,50 363,0 333,0 246,37 163,0" fill="var(--navy)"/>
      <polygon points="133,270 246,220 363,270 333,270 246,233 163,270" fill="var(--white)"/>
    </svg>
    <div class="brand-name">Birchford Realty</div>
    <div class="details">
      <div class="agent-name">Jordan Ellis</div>
      <div class="agent-title">Broker · License No. 5839162</div>
      <address class="address">7218 Crestover Ave E<br>Saginaw, MI 48271</address>
      <ul class="contact-list">
        <li>office phone :&nbsp; 555-5555</li>
        <li>cell phone: 555-5555</li>
        <li>email: jordan@BirchfordRealty.example</li>
        <li>web: BirchfordRealty.example</li>
      </ul>
    </div>
  </section>
</main>
</body>
</html>
```